Business cards for KORBEN Real Estate Properties LLC

We need a cool, original business card design for a company based in the Washington DC metropolitan area. We are a new energetic and passionate Real Estate Investing Company that invests in all types of real estate; commercial, residential, industrial etc.

Our company color is Red since it reflects action, energy and speed; it is assertive confident, energizing, exciting, powerful, passionate and determined. So we would like business card communicate those qualities to the audience.

Our audiences are investors that want to invest with us, real estate sellers, buyers, and tenants who lease from us.

Our logo is attached

```html
<!DOCTYPE html>
<html lang="en">
<head>
<meta charset="utf-8">
<title>KORBEN Real Estate Properties LLC — Business Cards</title>
<link rel="stylesheet" href="https://fonts.googleapis.com/css2?family=Questrial&family=Montserrat:wght@700&display=swap">
<style>
  :root {
    --red: #d7222f;
    --red-dark: #b8141f;
    --red-light: #e8434f;
    --white: #ffffff;
    --paper: #f4f4f4;
    --ink: #3a3a3a;
    --grey: #8a8a8a;
    --stage: #e9e6e1;
  }
  * { box-sizing: border-box; margin: 0; padding: 0; }
  html, body {
    width: 1171px; height: 1200px; overflow: hidden;
    background: var(--stage);
  }
  .sheet {
    position: relative; width: 1171px; height: 1200px;
    display: flex; justify-content: center; align-items: center; gap: 70px;
  }
  .card {
    position: relative; width: 440px; height: 770px; overflow: hidden;
    background: var(--white);
    box-shadow: 0 10px 30px rgba(0,0,0,.18);
    font-family: "Questrial", sans-serif;
  }

  /* ---------- front ---------- */
  .holder { position: absolute; top: 44px; right: 40px; text-align: left; color: var(--grey); }
  .holder__name { font-size: 30px; }
  .holder__role { font-size: 18px; margin-top: 2px; }

  .brand {
    position: absolute; top: 200px; left: 40px; right: 30px;
    display: flex; align-items: center; gap: 16px;
  }
  .brand__dot { width: 46px; height: 46px; border-radius: 50%; background: var(--red); flex: none; }
  .brand__name { font-size: 24px; line-height: 1.2; color: var(--ink); text-transform: uppercase; letter-spacing: .5px; }

  .skyline {
    position: absolute; left: 0; right: 0; height: 70px;
    background: linear-gradient(to bottom, rgba(215,34,47,0), var(--red));
  }
  .front .skyline { top: 360px; }
  .front .panel {
    position: absolute; top: 430px; left: 0; right: 0; bottom: 0;
    background: linear-gradient(160deg, var(--red-light), var(--red) 45%, var(--red-dark));
    padding: 46px 36px 0 40px; color: var(--white);
  }
  .contact { list-style: none; }
  .contact li { display: flex; align-items: flex-start; gap: 18px; font-size: 17px; line-height: 1.35; margin-bottom: 16px; }
  .contact svg { width: 24px; height: 24px; flex: none; fill: none; stroke: var(--white); stroke-width: 1.8; stroke-linecap: round; stroke-linejoin: round; }

  /* ---------- back ---------- */
  .back .panel {
    position: absolute; top: 0; left: 0; right: 0; height: 400px;
    background: linear-gradient(160deg, var(--red-light), var(--red) 45%, var(--red-dark));
    display: flex; align-items: center; justify-content: center;
  }
  .headline {
    font-family: "Montserrat", sans-serif; font-weight: 700;
    color: var(--white); text-align: center; text-transform: uppercase;
    font-size: 44px; line-height: 1.18; letter-spacing: 2px; margin-top: -30px;
  }
  .headline span { display: block; }
  .headline .wide { letter-spacing: 9px; }
  .back .skyline { top: 400px; background: linear-gradient(to bottom, var(--red), rgba(215,34,47,0)); }
  .back .brand { top: auto; bottom: 150px; left: 0; right: 0; justify-content: center; flex-direction: column; gap: 18px; }
  .back .brand__dot { width: 110px; height: 110px; }
  .back .brand__name { font-size: 40px; letter-spacing: 6px; }
</style>
</head>
<body>
<main class="sheet">

  <section class="card front" aria-label="Card front">
    <div class="holder">
      <p class="holder__name">Your Name</p>
      <p class="holder__role">Designation</p>
    </div>

    <div class="brand">
      <span class="brand__dot"></span>
      <p class="brand__name">KORBEN Real Estate Properties LLC</p>
    </div>

    <div class="skyline" role="img" aria-label="City skyline silhouette"></div>

    <div class="panel">
      <ul class="contact">
        <li>
          <svg viewBox="0 0 24 24"><path d="M12 22s7-7 7-12a7 7 0 0 0-14 0c0 5 7 12 7 12z"/><circle cx="12" cy="10" r="2.5"/></svg>
          <span>Crestline Holdings, LLC, 4120 N.<br>Harbor Ave. #210, Arlington,<br>VA 22201</span>
        </li>
        <li>
          <svg viewBox="0 0 24 24"><rect x="7" y="2" width="10" height="20" rx="2"/><line x1="11" y1="18" x2="13" y2="18"/></svg>
          <span>202-555-0143</span>
        </li>
        <li>
          <svg viewBox="0 0 24 24"><path d="M3 9c0-3 4-4 9-4s9 1 9 4l-3 1-1-2H7L6 10z"/><rect x="5" y="11" width="14" height="9" rx="1"/><circle cx="12" cy="15.5" r="2"/></svg>
          <span>202-555-0178</span>
        </li>
        <li>
          <svg viewBox="0 0 24 24"><rect x="3" y="5" width="18" height="14" rx="1"/><path d="M3 6l9 7 9-7"/></svg>
          <span>alex@korbenproperties.com</span>
        </li>
        <li>
          <svg viewBox="0 0 24 24"><circle cx="12" cy="12" r="9"/><path d="M3 12h18M12 3c3 3 3 15 0 18M12 3c-3 3-3 15 0 18"/></svg>
          <span>www.korbenproperties.com</span>
        </li>
      </ul>
    </div>
  </section>

  <section class="card back" aria-label="Card back">
    <div class="panel">
      <h1 class="headline">
        <span>Looking for</span>
        <span class="wide">Best deals</span>
        <span>in property ?</span>
      </h1>
    </div>
    <div class="skyline" role="img" aria-label="City skyline silhouette"></div>

    <div class="brand">
      <span class="brand__dot"></span>
      <p class="brand__name">KORBEN</p>
    </div>
  </section>

</main>
</body>
</html>
```